Label For Hand soap

Hello,

I would like to get your assistance with creating a label for my hand soap that I am in the process of developing. I would like the label to look simple visually appealing and eye catching similar to a cologne bottle's label. I would like there to be graphic or illustration accompanied with the text. The color scheme is black. I would like the background of the label to be transparent so that I can show the color of my product. I have attached some pictures of my bottle and some labels that I like for your reference. The name of my brand is Vrell. The hand soap scent is candied pineapples.

Thanks

```html
<!DOCTYPE html>
<html lang="en">
<head>
<meta charset="utf-8">
<title>Vrell Hand Wash Soap Label</title>
<link rel="stylesheet" href="https://fonts.googleapis.com/css2?family=Oswald:wght@400;600&family=Courgette&display=swap">
<style>
  :root {
    --page: #ffffff;
    --label: #0b0b0b;
    --ink: #ffffff;
    --art-light: #ffffff;
    --art-shade: #e4e4e4;
  }
  * { margin: 0; padding: 0; box-sizing: border-box; }
  html, body {
    width: 846px;
    height: 1200px;
    overflow: hidden;
    background: var(--page);
  }
  .canvas {
    position: relative;
    width: 846px;
    height: 1200px;
  }
  .label {
    position: absolute;
    left: 123px;
    top: 290px;
    width: 600px;
    height: 620px;
  }
  .label-shape {
    position: absolute;
    inset: 0;
  }
  .label-content {
    position: absolute;
    inset: 0;
    display: flex;
    flex-direction: column;
    align-items: center;
    color: var(--ink);
    text-align: center;
  }
  .pineapple-art {
    margin-top: 62px;
    width: 140px;
    height: 205px;
    border-radius: 46% 46% 50% 50% / 30% 30% 60% 60%;
    background: linear-gradient(180deg, var(--art-light), var(--art-shade));
  }
  .brand-name {
    margin-top: 6px;
    font-family: "Oswald", sans-serif;
    font-weight: 600;
    font-size: 118px;
    line-height: 1;
    letter-spacing: 2px;
  }
  .product-type {
    margin-top: 10px;
    font-family: "Oswald", sans-serif;
    font-weight: 400;
    font-size: 36px;
    line-height: 1;
    letter-spacing: 0.5px;
  }
  .scent {
    margin-top: 22px;
    font-family: "Courgette", cursive;
    font-size: 38px;
    line-height: 1.12;
  }
</style>
</head>
<body>
<main class="canvas">
  <section class="label">
    <svg class="label-shape" width="600" height="620" viewBox="0 0 600 620" aria-hidden="true">
      <path fill="var(--label)" d="M34 0 H566 A34 34 0 0 0 600 34 V586 A34 34 0 0 0 566 620 H34 A34 34 0 0 0 0 586 V34 A34 34 0 0 0 34 0 Z"/>
      <path fill="none" stroke="var(--ink)" stroke-width="2.5" d="M42 16 H558 A26 26 0 0 0 584 42 V578 A26 26 0 0 0 558 604 H42 A26 26 0 0 0 16 578 V42 A26 26 0 0 0 42 16 Z"/>
    </svg>
    <div class="label-content">
      <div class="pineapple-art" role="img" aria-label="White pineapple illustration with crossed diamond pattern and leafy crown"></div>
      <h1 class="brand-name">Vrell</h1>
      <p class="product-type">HAND WASH SOAP</p>
      <p class="scent">Candied Pineapples<br>Scent</p>
    </div>
  </section>
</main>
</body>
</html>
```